New Letterhead

Improve the attached letterhead to make it more alive and corporate class using the company colors in the two companies logos available on the two companies website.

Industry/Entity Type

Construction Company

Requirements
Must have
• colours of the two logod
Nice to have
• Be more alive and professional
Should not have
• Any other colours besides the ones in the logos

```html
<!DOCTYPE html>
<html lang="en">
<head>
<meta charset="utf-8">
<title>KMR VT Letterhead</title>
<link rel="stylesheet" href="https://fonts.googleapis.com/css2?family=Roboto:wght@400&family=Montserrat:wght@400;600;700;800&family=Great+Vibes&display=swap">
<style>
  :root {
    --ink: #2b2f33;
    --body: #3a3a3a;
    --brick: #8a2a1c;
    --teal: #2e8b93;
    --paper: #ffffff;
    --rule: #2b2f33;
  }
  * { margin: 0; padding: 0; box-sizing: border-box; }
  html, body { width: 848px; height: 1200px; overflow: hidden; background: var(--paper); }
  .sheet { position: relative; width: 848px; height: 1200px; background: var(--paper); }

  .letter { position: absolute; left: 76px; top: 94px; width: 508px;
    font-family: "Roboto", Arial, sans-serif; font-size: 12.6px; line-height: 22px; color: var(--body); }
  .letter p { margin-bottom: 22px; }
  .letter .recipient { margin-bottom: 44px; }
  .letter .closing { margin-bottom: 0; }
  .signature { font-family: "Great Vibes", cursive; font-size: 40px; line-height: 62px; color: var(--ink); margin-top: -2px; }
  .signer { line-height: 21px; margin-top: -2px; }

  .divider { position: absolute; left: 606px; top: 25px; width: 1px; height: 1100px; background: var(--rule); }

  .side { position: absolute; left: 632px; width: 200px; font-family: "Montserrat", Arial, sans-serif; color: var(--ink); }
  .brand-name { font-weight: 800; font-size: 30px; line-height: 32px; letter-spacing: 1px; color: var(--ink); }
  .tagline { margin-top: 10px; font-weight: 700; font-size: 10.5px; line-height: 15px; text-transform: uppercase; }
  .tagline .accent { color: var(--brick); }

  .office-name { font-weight: 800; font-size: 21px; line-height: 24px; }
  .office-name.kestrel { color: var(--ink); }
  .office-name.tembani { color: var(--brick); font-size: 19px; }
  .office { font-size: 10px; line-height: 14px; margin-top: 6px; }
  .office .entity { font-weight: 700; }
  .contacts { list-style: none; margin-top: 6px; font-size: 10px; line-height: 14px; }
  .contacts li { display: flex; align-items: center; gap: 5px; }
  .contacts svg { width: 8px; height: 8px; flex: none; }
  .contacts.teal svg { fill: var(--teal); stroke: var(--teal); }
  .contacts.brick svg { fill: var(--brick); stroke: var(--brick); }

  .legal { font-size: 8.5px; line-height: 14px; }
  .legal .directors { margin-top: 8px; display: grid; grid-template-columns: auto auto; column-gap: 5px; justify-content: start; }
</style>
</head>
<body>
<div class="sheet">

  <main class="letter">
    <p class="date">October 22, 2018</p>
    <p class="recipient">Mr. John Doe<br>123 Main Street SW<br>Dallas, TX 75229</p>
    <p>Dear Mr. Doe,</p>
    <p>Lorem ipsum dolor sit amet, consectetur adipiscing elit. Mauris vitae sapien quis sapien maximus commodo. Ut placerat posuere cursus. Nullam justo erat, iaculis quis pellentesque ut, tempus eget tortor. Nulla volutpat libero leo, id tempus massa venenatis porttitor. Donec eget nulla id orci vestibulum congue. Nulla nulla tellus, mattis a auctor at, mattis at quam. Aenean posuere imperdiet felis, nec condimentum diam. Maecenas lacinia, magna vel ultrices scelerisque, purus arcu vehicula metus, volutpat eleifend diam sem id nisi. Suspendisse potenti. Vestibulum ante ipsum primis in faucibus orci luctus et ultrices posuere cubilia Curae; Nam sollicitudin volutpat ante utlacus n varius justo porta vitae.</p>
    <p>Vivamus interdum dui a nulla efficitur egestas. Quisque dignissim tincidunt mauris. Curabitur eu nulla ex. Sed at dolor ligula. Pellentesque felis diam, malesuada eget velit vel, laoreet efficitur ligula.Suspendisse nec ipsum lacus. Aliquam imperdiet lobortis magna eget sagittis. Aliquam commodo magna consectetur pharetra consectetur. Interdum et malesuada fames ac ante ipsum primis in faucibus. Nulla consectetur, neque at lobortis porttitor, dolor risus sagittis lacus, nec efficitur ante nisi sed nisi. Etiam quis dapibus lorem. In quis sodales augue, in eleifend urna. Duis hendrerit risus mauris, vitae posuere elit lacinia vitae. Lorem ipsum dolor sit amet, consectetur adipiscing elit ivamus eget nunc.</p>
    <p>Morbi blandit lorem nisi, non dapibus tellus venenatis consequat. Interdum et malesuada fames ac ante ipsum primis in faucibus. Suspendisse non convallis purus, ac pretium ligula. Praesent molestie justo at nibh eleifend, rutrum aliquet leo sagittis. In semper erat ac facilisis tempus. Cras cursus magna nec dolor tincidunt commodo. In cursus, ex non molestie pellentesque, dolor sapien vulputate diam, non maximus sem sem at sapien. Cras tempor sit amet sem vestibulum sodales. Aliquam placerat, purus quis pharetra aliquet, ligula nulla luctus arcu, eu volutpat orci libero vel justo. Phasellus rhoncus lobortis mauris ut rutrum. Mauris lectus ligula, fringilla in quam in, imperdiet lobortis nibh aecenas justo.</p>
    <p class="closing">Regards,</p>
    <div class="signature">Signature</div>
    <p class="signer">Your Name<br>Title</p>
  </main>

  <div class="divider"></div>

  <header class="side" style="top:46px;">
    <div class="brand-name">KMR VT</div>
    <p class="tagline">Building sound<br>structures with care,<br>lasting value, <span class="accent">every project</span></p>
  </header>

  <section class="side" style="top:662px;">
    <div class="office-name kestrel">KESTREL</div>
    <p class="office"><span class="entity">KMR VT JV (Pty) Limited</span><br>7 Marula Lane<br>Rosebank, Johannesburg<br>PO Box 51290, Parkhurst, 2120<br>South Africa</p>
    <ul class="contacts teal">
      <li><svg viewBox="0 0 10 10"><path d="M2 0.5 L4 2.5 L3 4 Q4.5 6 6 7 L7.5 6 L9.5 8 L8 9.5 Q3.5 9 0.5 2 Z" stroke="none"/></svg>+27 (0)11 555 0142</li>
      <li><svg viewBox="0 0 10 10"><rect x="0.5" y="2" width="9" height="6.5" stroke="none"/><path d="M0.8 2.3 L5 5.6 L9.2 2.3" fill="none" stroke="#fff" stroke-width="1"/></svg>info@kestrelbuild.com</li>
      <li><svg viewBox="0 0 10 10" fill="none"><circle cx="5" cy="5" r="4.2" fill="none" stroke-width="1"/><ellipse cx="5" cy="5" rx="1.8" ry="4.2" fill="none" stroke-width="0.8"/><path d="M0.8 5 H9.2" stroke-width="0.8"/></svg>www.kestrelbuild.com</li>
    </ul>
  </section>

  <section class="side" style="top:845px;">
    <div class="office-name tembani">TEMBANI GROUP</div>
    <p class="office"><span class="entity">KMR VT JV (Pty) Limited</span><br>22 Acacia Road<br>Cnr Oxford Avenue<br>Melrose North,<br>Johannesburg 2196<br>South Africa</p>
    <ul class="contacts brick">
      <li><svg viewBox="0 0 10 10"><path d="M2 0.5 L4 2.5 L3 4 Q4.5 6 6 7 L7.5 6 L9.5 8 L8 9.5 Q3.5 9 0.5 2 Z" stroke="none"/></svg>+27 (0)11 555 0198</li>
      <li><svg viewBox="0 0 10 10"><rect x="0.5" y="2" width="9" height="6.5" stroke="none"/><path d="M0.8 2.3 L5 5.6 L9.2 2.3" fill="none" stroke="#fff" stroke-width="1"/></svg>info@tembani.com</li>
      <li><svg viewBox="0 0 10 10" fill="none"><circle cx="5" cy="5" r="4.2" fill="none" stroke-width="1"/><ellipse cx="5" cy="5" rx="1.8" ry="4.2" fill="none" stroke-width="0.8"/><path d="M0.8 5 H9.2" stroke-width="0.8"/></svg>www.tembani.com</li>
    </ul>
  </section>

  <footer class="side legal" style="top:1040px;">
    <p>Registration No. 2017/000123/07<br>Trading as KMR VT JV (Pty) Limited</p>
    <div class="directors"><span>Directors:</span><span>Peter Walsh<br>Thabo Sipho Ndlovu</span></div>
  </footer>

</div>
</body>
</html>
```